Flyer Design

I'm looking for a new flyer design to help promote our landscape company, and some of our main service for the up and coming season. We're trying to position ourselves as a leader in our market, so obviously quality is important to us.

Our current promotion is 25% off the first month with signup of annual service.

Phone Number: (816) 555-0193
Website: gardelvista.com
Our tagline: "Your hands are full... Let us help"

The call to action: direct them to our website for a detailed list of services and to receive a free quote.

You're welcome to add your own wording and punctuation. If I like the design I will provide feedback accordingly.

I have attached a jpg of our logo to help with design colors. I will provide the vector file upon completion of this project.

Also, I've attached a few photos that I had on hand of our companies work that may help with the design. Obviously I don't want to use them all, but there are a couple just to help out. I'm not opposed to stock photos either.
Thanks

Target Market(s)

We market to high end customers, generally with home between $500k-$2mil, or household income over $200k. Quality and creativity are most important to us.

Industry/Entity Type

Landscape

Requirements
Must have
• Creativity, easy to read, modern style.

```html
<!DOCTYPE html>
<html lang="en">
<head>
<meta charset="utf-8">
<title>Gardel Vista Flyer</title>
<link href="https://fonts.googleapis.com/css2?family=Oswald:wght@400;500;600;700&family=Roboto+Condensed:wght@400;700&display=swap" rel="stylesheet">
<style>
  :root {
    --orange: #ec5a1e;
    --orange-deep: #c63c0f;
    --orange-light: #ff7a38;
    --ink: #161616;
    --charcoal: #2a2a2a;
    --steel: #3a3a3a;
    --white: #ffffff;
    --grey-text: #d9d9d9;
  }
  * { margin: 0; padding: 0; box-sizing: border-box; }
  html, body { width: 900px; height: 1200px; overflow: hidden; background: #ececec; }
  .flyer {
    position: relative;
    width: 900px;
    height: 1200px;
    overflow: hidden;
    background: var(--ink);
    font-family: "Roboto Condensed", "Arial Narrow", sans-serif;
    color: var(--white);
  }
  .flyer-shapes { position: absolute; inset: 0; }

  .brand-badge {
    position: absolute;
    left: 40px; top: 160px;
    width: 180px; height: 180px;
    border-radius: 50%;
    background: var(--white);
    border: 10px solid var(--orange);
    display: flex; align-items: center; justify-content: center;
    box-shadow: 0 6px 18px rgba(0,0,0,.45);
  }
  .brand-name {
    font-family: "Oswald", sans-serif;
    font-weight: 700;
    font-size: 30px;
    line-height: 1;
    text-align: center;
    color: var(--charcoal);
    text-transform: uppercase;
  }

  .tagline {
    position: absolute;
    left: 150px; top: 430px;
    width: 600px;
    text-align: center;
  }
  .tagline-lead {
    display: inline-block;
    background: linear-gradient(#3c3c3c, #1b1b1b);
    border-radius: 14px 14px 0 0;
    padding: 6px 34px 4px;
    font-family: "Oswald", sans-serif;
    font-weight: 600;
    font-style: italic;
    font-size: 34px;
    letter-spacing: 1px;
    text-transform: uppercase;
    width: 560px;
  }
  .tagline-main {
    display: block;
    background: linear-gradient(#4a4a4a, #262626);
    border: 3px solid #6a6a6a;
    border-radius: 16px;
    padding: 2px 0 6px;
    font-family: "Oswald", sans-serif;
    font-weight: 500;
    font-size: 84px;
    line-height: 1.1;
    color: var(--orange-light);
    text-transform: uppercase;
    box-shadow: 0 8px 18px rgba(0,0,0,.5);
  }

  .services-title {
    position: absolute;
    left: 330px; top: 602px;
    width: 240px; height: 52px;
    background: var(--ink);
    border: 3px solid var(--white);
    border-radius: 26px;
    display: flex; align-items: center; justify-content: center;
    font-family: "Oswald", sans-serif;
    font-weight: 700;
    font-style: italic;
    font-size: 30px;
    letter-spacing: 1px;
    text-transform: uppercase;
  }

  .service-list {
    position: absolute;
    left: 0; top: 675px;
    width: 900px; height: 270px;
    display: grid;
    grid-template-columns: repeat(4, 1fr);
    list-style: none;
  }
  .service-item {
    display: flex; flex-direction: column; align-items: center;
    padding-top: 26px;
    border-right: 2px solid #444;
  }
  .service-item:last-child { border-right: none; }
  .service-label {
    height: 70px;
    font-weight: 700;
    font-size: 24px;
    line-height: 1.1;
    text-align: center;
    text-transform: uppercase;
    color: var(--grey-text);
    display: flex; align-items: center;
  }
  .service-icon {
    width: 120px; height: 120px;
    border-radius: 50%;
    background: var(--orange);
    display: flex; align-items: center; justify-content: center;
    margin-top: 20px;
  }
  .service-icon svg { width: 70px; height: 70px; }

  .contact {
    position: absolute;
    left: 0; top: 1000px;
    width: 900px;
    text-align: center;
  }
  .contact-phone {
    display: inline-block;
    background: var(--ink);
    border-radius: 28px;
    padding: 6px 46px;
    font-family: "Oswald", sans-serif;
    font-weight: 600;
    font-size: 44px;
    color: var(--orange-light);
  }
  .contact-web {
    display: block;
    margin-top: 10px;
    font-family: "Oswald", sans-serif;
    font-weight: 600;
    font-size: 46px;
    color: var(--white);
  }

  .offer-badge {
    position: absolute;
    left: 660px; top: 980px;
    width: 190px; height: 190px;
    border-radius: 50%;
    background: radial-gradient(circle at 40% 35%, #ffffff, #dcdcdc);
    border: 6px solid #bdbdbd;
    box-shadow: 0 6px 16px rgba(0,0,0,.5);
    display: flex; flex-direction: column; align-items: center; justify-content: center;
    color: var(--orange);
    font-family: "Oswald", sans-serif;
  }
  .offer-amount { display: flex; align-items: center; font-weight: 700; font-size: 70px; line-height: .9; }
  .offer-off {
    font-size: 22px; font-weight: 600;
    writing-mode: vertical-rl; transform: rotate(180deg);
    margin-left: 4px;
  }
  .offer-terms {
    margin-top: 4px;
    font-size: 18px; font-weight: 500;
    color: var(--ink);
    background: var(--white);
    text-transform: uppercase;
  }
</style>
</head>
<body>
<main class="flyer">
  <svg class="flyer-shapes" viewBox="0 0 900 1200" width="900" height="1200" aria-hidden="false">
    <defs>
      <linearGradient id="photoTone" x1="0" y1="0" x2="1" y2="1">
        <stop offset="0" stop-color="#cfd6dd"/>
        <stop offset=".45" stop-color="#8a2a22"/>
        <stop offset=".75" stop-color="#3a2a2a"/>
        <stop offset="1" stop-color="#e6eaee"/>
      </linearGradient>
      <linearGradient id="orangeField" x1="0" y1="0" x2="0" y2="1">
        <stop offset="0" stop-color="#f06a2a"/>
        <stop offset="1" stop-color="#c53b0e"/>
      </linearGradient>
      <linearGradient id="bandTone" x1="0" y1="0" x2="0" y2="1">
        <stop offset="0" stop-color="#2f2f2f"/>
        <stop offset="1" stop-color="#1e1e1e"/>
      </linearGradient>
    </defs>
    <rect width="900" height="1200" fill="#161616"/>
    <path d="M0 330 C300 300 600 260 900 240 V1200 H0 Z" fill="url(#orangeField)" role="img" aria-label="Orange textured background"/>
    <path d="M0 0 H900 V300 C620 330 320 380 0 420 Z" fill="url(#photoTone)" role="img" aria-label="Photo of a red pickup truck with a snow plow clearing a snowy driveway"/>
    <path d="M0 420 C320 380 620 330 900 300" fill="none" stroke="#ffffff" stroke-width="4"/>
    <rect x="0" y="675" width="900" height="270" fill="url(#bandTone)"/>
    <path d="M0 1150 C300 1120 600 1120 900 1160 V1200 H0 Z" fill="#161616"/>
  </svg>

  <div class="brand-badge"><span class="brand-name">Gardel<br>Vista</span></div>

  <div class="tagline">
    <span class="tagline-lead">Your hands are full...</span>
    <span class="tagline-main">Let us help</span>
  </div>

  <div class="services-title">Services</div>

  <ul class="service-list">
    <li class="service-item">
      <span class="service-label">Mowing</span>
      <span class="service-icon">
        <svg viewBox="0 0 70 70" fill="#fff">
          <path d="M14 12 L28 36 L24 38 L10 14 Z"/>
          <rect x="18" y="34" width="40" height="16" rx="4"/>
          <circle cx="24" cy="54" r="7"/>
          <circle cx="52" cy="54" r="7"/>
        </svg>
      </span>
    </li>
    <li class="service-item">
      <span class="service-label">Tree<br>Maintenance</span>
      <span class="service-icon">
        <svg viewBox="0 0 70 70" fill="none" stroke="#fff" stroke-width="4">
          <path d="M35 8 C20 8 12 20 16 32 C10 40 18 50 28 46 C32 50 38 50 42 46 C52 50 60 40 54 32 C58 20 50 8 35 8 Z"/>
          <path d="M35 30 V64 M35 40 L27 34 M35 44 L44 37" stroke-linecap="round"/>
        </svg>
      </span>
    </li>
    <li class="service-item">
      <span class="service-label">Aeration</span>
      <span class="service-icon">
        <svg viewBox="0 0 70 70" fill="#fff">
          <g>
            <rect x="12" y="14" width="6" height="10" rx="3"/><rect x="26" y="14" width="6" height="10" rx="3"/><rect x="40" y="14" width="6" height="10" rx="3"/><rect x="54" y="14" width="6" height="10" rx="3"/>
            <rect x="12" y="30" width="6" height="10" rx="3"/><rect x="26" y="30" width="6" height="10" rx="3"/><rect x="40" y="30" width="6" height="10" rx="3"/><rect x="54" y="30" width="6" height="10" rx="3"/>
            <rect x="12" y="46" width="6" height="10" rx="3"/><rect x="26" y="46" width="6" height="10" rx="3"/><rect x="40" y="46" width="6" height="10" rx="3"/><rect x="54" y="46" width="6" height="10" rx="3"/>
          </g>
        </svg>
      </span>
    </li>
    <li class="service-item">
      <span class="service-label">Snow<br>Removal</span>
      <span class="service-icon">
        <svg viewBox="0 0 70 70" fill="none" stroke="#fff" stroke-width="4" stroke-linecap="round">
          <path d="M18 42 C8 42 8 28 18 28 C20 16 38 14 42 24 C54 22 60 34 52 42 Z"/>
          <path d="M24 52 V62 M19 57 H29 M46 52 V62 M41 57 H51 M35 50 V58 M31 54 H39"/>
        </svg>
      </span>
    </li>
  </ul>

  <div class="contact">
    <span class="contact-phone">(816) 555-0193</span>
    <span class="contact-web">www.gardelvista.com</span>
  </div>

  <div class="offer-badge">
    <span class="offer-amount">25%<span class="offer-off">OFF</span></span>
    <span class="offer-terms">The first month</span>
  </div>
</main>
</body>
</html>
```